Copper Meadow Dental Lab - Presentation Folder Design

1. We are a dental lab providing a full range of dental products to restore and enhance the natural beauty of the patients’ smiles. We provide fixed restorations (Full-Contour Solid Zirconia, KRT o.lumo, Dune Prime, Full Cast, PFM, Temporary Crowns, Diagnostic Wax-Ups and Study Models), implant restorations (Single and Multi Tooth Restorations, Zirconia Prosthesis, Full Arch Hybrid Prosthesis), and
removable restorations (Dentures and Partials, PolyBend, Kernalite).
2. The target market are dentists, oral surgeons, implant manufacturers, and etc. We are not targeting patients.
3. Design specifics - no specifics, but I have provided our logo for reference if needed

Target Market(s)

Dentists, Oral Surgeons, implant manufacturers

Industry/Entity Type

Dental

Requirements
Must have
• Name - Copper Meadow Dental Lab, address - 4126 Orchard Ln, Suite 310, Fairbrook, ST 00123, office number - 555-555-0142, fax number - 555-555-0143, email - info@cmdentalworks.example

```html
<!DOCTYPE html>
<html lang="en">
<head>
<meta charset="utf-8">
<title>Copper Meadow Dental Lab – Presentation Folder</title>
<link rel="stylesheet" href="https://fonts.googleapis.com/css2?family=Oswald:wght@500&family=Open+Sans:wght@400;600&display=swap">
<style>
  :root {
    --navy-deep: #1f1f6e;
    --navy: #2e2f8f;
    --indigo: #3d3fa6;
    --violet: #5a5cc2;
    --sky: #cfe3f3;
    --white: #ffffff;
    --soft-text: #d7d8f2;
    --page-bg: #e9e9ea;
  }
  * { box-sizing: border-box; margin: 0; padding: 0; }
  html, body { width: 1200px; height: 902px; overflow: hidden; }
  body {
    background: var(--page-bg);
    font-family: "Open Sans", Arial, sans-serif;
    position: relative;
  }
  .folder {
    position: absolute;
    left: 80px; top: 83px;
    width: 1040px; height: 736px;
    display: flex;
  }
  .panel { position: relative; width: 520px; height: 736px; overflow: hidden; }

  /* Back panel */
  .panel-back {
    background: linear-gradient(160deg, var(--indigo) 0%, var(--navy) 45%, var(--navy-deep) 100%);
    color: var(--white);
    text-align: center;
    padding: 150px 60px 0;
  }
  .brand-mark {
    font-family: "Oswald", Arial, sans-serif;
    font-weight: 500;
    color: var(--white);
    letter-spacing: 2px;
    line-height: 1.05;
    text-transform: uppercase;
  }
  .panel-back .brand-mark { font-size: 34px; }
  .brand-mark .sub { display: block; font-size: 0.55em; letter-spacing: 4px; }
  .intro {
    margin-top: 42px;
    font-size: 11px;
    line-height: 1.6;
    color: var(--soft-text);
  }
  .intro p + p { margin-top: 12px; }
  .company-name {
    margin-top: 40px;
    font-family: "Oswald", Arial, sans-serif;
    font-weight: 500;
    font-size: 19px;
    letter-spacing: 1px;
    text-transform: uppercase;
  }
  .contact-grid {
    margin-top: 22px;
    display: grid;
    grid-template-columns: 215px 170px;
    gap: 16px 15px;
    text-align: left;
    font-size: 10.5px;
    line-height: 1.45;
    color: var(--soft-text);
  }
  .contact-item { display: flex; align-items: flex-start; gap: 8px; white-space: nowrap; }
  .contact-item svg { flex: none; width: 14px; height: 14px; }

  /* Front panel */
  .panel-front { background: var(--navy); }
  .front-art { position: absolute; inset: 0; }
  .panel-front .brand-mark {
    position: absolute;
    top: 46px; left: 0; right: 0;
    text-align: center;
    font-size: 38px;
  }
  .tagline {
    position: absolute;
    top: 588px; left: 0; right: 0;
    text-align: center;
    font-family: "Oswald", Arial, sans-serif;
    font-weight: 500;
    font-size: 30px;
    letter-spacing: 1px;
    color: var(--indigo);
  }
  .web-pill {
    position: absolute;
    top: 648px; left: 70px; right: 70px;
    height: 38px;
    border-radius: 19px;
    background: var(--indigo);
    color: var(--white);
    font-size: 17px;
    letter-spacing: 2px;
    line-height: 38px;
    text-align: center;
  }
</style>
</head>
<body>
  <main class="folder">
    <section class="panel panel-back">
      <div class="brand-mark">Copper Meadow<span class="sub">Dental Lab</span></div>
      <div class="intro">
        <p>We are a dental lab providing a full range of dental products to restore and enhance the natural beauty of the patients’ smiles.</p>
        <p>Our team blends skilled hands with modern digital workflows, delivering precise fixed, implant and removable restorations on schedule, with friendly support for every case and clinician we serve.</p>
      </div>
      <h2 class="company-name">Copper Meadow Dental Lab</h2>
      <div class="contact-grid">
        <div class="contact-item">
          <svg viewBox="0 0 14 14"><rect x="1" y="3" width="12" height="8" rx="1" fill="none" stroke="#fff" stroke-width="1.2"/><path d="M1 3l6 5 6-5" fill="none" stroke="#fff" stroke-width="1.2"/></svg>
          <span>info@cmdentalworks.example</span>
        </div>
        <div class="contact-item">
          <svg viewBox="0 0 14 14"><path d="M7 13s-4-4.5-4-7.5a4 4 0 0 1 8 0C11 8.5 7 13 7 13z" fill="#fff"/><circle cx="7" cy="5.5" r="1.5" fill="#2e2f8f"/></svg>
          <span>4126 Orchard Ln, Suite 310,<br>Fairbrook, ST 00123</span>
        </div>
        <div class="contact-item">
          <svg viewBox="0 0 14 14"><path d="M3 1.5l2.2 0 1 3-1.4 1.2a7 7 0 0 0 3.5 3.5l1.2-1.4 3 1v2.2c0 .6-.5 1-1 1A10.5 10.5 0 0 1 2 2.5c0-.5.4-1 1-1z" fill="#fff"/></svg>
          <span>555-555-0142 · Fax 555-555-0143</span>
        </div>
        <div class="contact-item">
          <svg viewBox="0 0 14 14"><circle cx="7" cy="7" r="6" fill="none" stroke="#fff" stroke-width="1.2"/><circle cx="7" cy="7" r="2" fill="#fff"/></svg>
          <span>@cmdentalworks</span>
        </div>
      </div>
    </section>

    <section class="panel panel-front">
      <svg class="front-art" viewBox="0 0 520 736" width="520" height="736">
        <defs>
          <linearGradient id="front-navy" x1="0" y1="0" x2="1" y2="1">
            <stop offset="0" stop-color="#3d3fa6"/>
            <stop offset="1" stop-color="#1f1f6e"/>
          </linearGradient>
          <radialGradient id="tooth-glow" cx="0.6" cy="0.45" r="0.7">
            <stop offset="0" stop-color="#ffffff"/>
            <stop offset="0.45" stop-color="#cfe3f3"/>
            <stop offset="1" stop-color="#8fb6d8"/>
          </radialGradient>
        </defs>
        <rect width="520" height="736" fill="url(#front-navy)"/>
        <path d="M52 372C100 228 300 168 520 162V580H52Z" fill="#5a5cc2"/>
        <path role="img" aria-label="Photo area: glossy white molar tooth wrapped in swirling light trails on a pale blue background" d="M72 380C120 250 310 190 520 184V580H72Z" fill="url(#tooth-glow)"/>
        <path d="M0 300C12 340 38 364 70 382C160 482 330 544 520 564V736H0Z" fill="#ffffff"/>
      </svg>
      <div class="brand-mark">Copper Meadow<span class="sub">Dental Lab</span></div>
      <p class="tagline">CREATING BEAUTIFUL SMILES</p>
      <p class="web-pill">www.cmdentalworks.example</p>
    </section>
  </main>
</body>
</html>
```